Thornvale plumbing business cards

Want a functional designed for my business cards using my logo

Company Name- Thornvale Plumbing, Heating & Water Systems
Name- Martin Thornvale
Title- Vice President
Cell- 555-318-7742
Email- Thornvaleplumbing@mailbrook.example
Business address-
PO Box 57
Corwin Hollow, KX 21990

Plumbing

```html
<!DOCTYPE html>
<html lang="en">
<head>
<meta charset="utf-8">
<title>Thornvale Plumbing – Business Card</title>
<link href="https://fonts.googleapis.com/css2?family=Roboto:wght@700&family=Source+Sans+3:wght@400;600&display=swap" rel="stylesheet">
<style>
  :root {
    --page-bg: #e9ecef;
    --card-blue: #0a6bbf;
    --card-black: #050505;
    --text-light: #ffffff;
    --badge-light: #f7f7f7;
    --badge-shade: #dcdfe2;
    --brand-ink: #1b1b1b;
  }
  html, body {
    margin: 0;
    width: 1200px;
    height: 900px;
    overflow: hidden;
    background: var(--page-bg);
  }
  .business-card {
    position: absolute;
    left: 110px;
    top: 147px;
    width: 980px;
    height: 606px;
    background: var(--card-black);
    overflow: hidden;
    box-shadow: 0 14px 40px rgba(0,0,0,0.18);
  }
  .blue-panel {
    position: absolute;
    left: 0; top: 0;
    width: 702px; height: 100%;
    background: var(--card-blue);
  }
  .contact-block {
    position: absolute;
    left: 59px; top: 0;
    width: 600px; height: 100%;
    color: var(--text-light);
    font-family: "Source Sans 3", sans-serif;
  }
  .person-name {
    position: absolute;
    top: 76px;
    margin: 0;
    white-space: nowrap;
    font-family: "Roboto", sans-serif;
    font-weight: 700;
    font-size: 33px;
    line-height: 40px;
    letter-spacing: 0.2px;
    text-transform: uppercase;
  }
  .person-title {
    position: absolute;
    top: 116px;
    margin: 0;
    white-space: nowrap;
    font-size: 25px;
    line-height: 36px;
  }
  .postal-address {
    position: absolute;
    top: 328px;
    margin: 0;
    font-style: normal;
    font-size: 25px;
    line-height: 35px;
    white-space: nowrap;
  }
  .contact-lines {
    position: absolute;
    top: 431px;
    margin: 0; padding: 0;
    list-style: none;
    font-size: 25px;
    line-height: 36px;
    white-space: nowrap;
  }
  .contact-lines li { display: flex; align-items: center; gap: 8px; }
  .contact-lines svg { width: 20px; height: 20px; fill: var(--text-light); flex: none; }
  .brand-badge {
    position: absolute;
    left: 430px; top: 56px;
    width: 526px; height: 526px;
    border-radius: 50%;
    background: radial-gradient(circle at 45% 40%, var(--badge-light) 0%, #eceeef 55%, var(--badge-shade) 100%);
    display: flex;
    align-items: center;
    justify-content: center;
  }
  .brand-name {
    margin: 0;
    font-family: "Source Sans 3", sans-serif;
    font-weight: 400;
    color: var(--brand-ink);
    text-align: center;
    line-height: 1.15;
  }
  .brand-name .line-main { display: block; font-size: 46px; }
  .brand-name .line-sub { display: block; font-size: 32px; }
</style>
</head>
<body>
  <section class="business-card" aria-label="Thornvale Plumbing business card">
    <div class="blue-panel"></div>
    <div class="contact-block">
      <h1 class="person-name">Martin Thornvale</h1>
      <p class="person-title">Vice President</p>
      <address class="postal-address">PO Box 57<br>Corwin Hollow, KX 21990</address>
      <ul class="contact-lines">
        <li>
          <svg viewBox="0 0 20 20" aria-hidden="true"><path d="M3 6c0-2 3-3 7-3s7 1 7 3v2h-4V6.5c-1-.4-2-.5-3-.5s-2 .1-3 .5V8H3z M5 9h10l2 8H3z M8 11h4v4H8z"/></svg>
          555.204.6613
        </li>
        <li>
          <svg viewBox="0 0 20 20" aria-hidden="true"><path d="M6 1h8a1 1 0 0 1 1 1v16a1 1 0 0 1-1 1H6a1 1 0 0 1-1-1V2a1 1 0 0 1 1-1zm1 3v11h6V4z"/></svg>
          555-318-7742
        </li>
        <li>
          <svg viewBox="0 0 20 20" aria-hidden="true"><path d="M2 4h16v12H2z M3 5l7 6 7-6" fill="none" stroke="#fff" stroke-width="1.6"/></svg>
          Thornvaleplumbing@mailbrook.example
        </li>
      </ul>
    </div>
    <div class="brand-badge">
      <p class="brand-name">
        <span class="line-main">Thornvale Plumbing</span>
        <span class="line-sub">Heating &amp; Water Systems</span>
      </p>
    </div>
  </section>
</body>
</html>
```